Sign Design

We already have a logo, but would like to design 2 x signs.
Sign 1:
Dimensions 1500mm wide x 2500m high.
Information to include on sign: - Clinic name and logo (attached)
- the word "DENTIST "
- Street number (which is 348)
Phone number (which is 6153 4097)

Sign 2:
Dimensions: 800mm wide x 600mm high

```html
<!DOCTYPE html>
<html lang="en">
<head>
<meta charset="utf-8">
<title>Kellerton Dental Care – Dentist Sign</title>
<link rel="stylesheet" href="https://fonts.googleapis.com/css2?family=Arimo:wght@400&family=Josefin+Sans:wght@300&family=Questrial&display=swap">
<style>
  :root {
    --green: #29b34b;
    --green-dark: #14713b;
    --green-pale: #ddeaae;
    --white: #ffffff;
  }
  html, body {
    margin: 0;
    padding: 0;
    width: 1200px;
    height: 722px;
    overflow: hidden;
    background: var(--white);
  }
  .sign {
    display: block;
    width: 1200px;
    height: 722px;
  }
  .banner-top { fill: var(--green); }
  .banner-bottom { fill: var(--green-pale); }
  .headline {
    font-family: "Josefin Sans", sans-serif;
    font-weight: 300;
    fill: var(--white);
  }
  .clinic-name {
    font-family: "Arimo", sans-serif;
    font-weight: 400;
    fill: var(--green-dark);
  }
  .contact {
    font-family: "Questrial", sans-serif;
    fill: var(--green);
  }
  .brand-dot {
    fill: var(--green-pale);
    stroke: var(--white);
    stroke-width: 9;
  }
</style>
</head>
<body>
<svg class="sign" viewBox="0 0 1200 722" xmlns="http://www.w3.org/2000/svg">
  <polygon class="banner-top" points="0,21 1174,21 1142,109 1174,198 0,198"/>
  <text class="headline" x="24" y="155" font-size="134" textLength="488" lengthAdjust="spacingAndGlyphs">DENTIST</text>

  <polygon class="banner-bottom" points="145,563 1200,563 1200,698 145,698 174,631"/>

  <circle class="brand-dot" cx="195" cy="385" r="165"/>

  <text class="clinic-name" x="419" y="378" font-size="158" textLength="757" lengthAdjust="spacingAndGlyphs">Kellerton</text>
  <text class="clinic-name" x="685" y="468" font-size="88" textLength="434" lengthAdjust="spacingAndGlyphs">Dental Care</text>

  <text class="contact" x="1173" y="626" font-size="66" text-anchor="end" letter-spacing="4">Street number 348</text>
  <text class="contact" x="1179" y="690" font-size="66" text-anchor="end" letter-spacing="4">Phone number 6153 4097</text>
</svg>
</body>
</html>
```